Zielgruppe
Das erzählende Sachbuch 'Allein. Getragen. Heiter. 7 frische Wege zu Fülle und Nähe abseits der Zweisamkeit' richtet sich an Frauen ohne Partner und Kinder.
Im Buch präsentiere ich sieben inspirierende Lebensentwürfe, die zeigen, wie auch ohne Partnerschaft und Familie ein sinnerfülltes Leben in tiefer Verbindung zu anderen möglich ist.
Das Buch lädt alle Frauen (und natürlich auch Männer) ein, anders zu denken und zu leben. Es ermächtigt die Leser:innen, eine liebevolle Perspektive auf ihr Sololeben einzunehmen und ihren eigenen, außergewöhnlichen Weg zu gehen, kurzum: glücklich-verbunden zu leben.
Die Zielgruppe sind moderne Frauen jeden Alters, die offen für das Thema Persönlichkeitsentwicklung sind und ihr Glück selbst in die Hand nehmen.
Aufgabenstellung
Text Cover:
Buchtitel: Allein. Getragen. Heiter.
Untertitel: 7 frische Wege zu Fülle und Nähe abseits der Zweisamkeit
Störer: Mit inspirierenden Tipps zur Umsetzung
Autorin: Jule Henrike Brandt
Format:
Das Buch wird als Taschenbuch bei WLV veröffentlicht, im Format 13,34 x 20,32 cm (5,25 x 8 Zoll). Die Vorlage für das Layout des Buchcovers (Titelseite, Seitenleiste, Rückseite) ist hier angehängt. Es wird benötigt: Titelseite, Seitenleiste, Rückseite mit Klappentext und Platzhalter für Barcode. Bitte beachten: Das Buch wird gerade gesetzt. Eventuell muss die Breite des Buchrückens am Ende noch angepasst werden, je nach finaler Seitenzahl.
Inhalt:
Das Cover soll eine Frau zeigen, da im Titel nicht explizit von Frauen gesprochen wird, die Zielgruppe des Buches aber Frauen sind. Diese soll eher schematisch dargestellt sein, damit möglichst viele Frauen sich mit ihr identifizieren können. Sie soll glücklich wirken. Falls Details zu sehen sind: mitteleuropäisch, Haarfarbe hellbraun, Augenfarbe blau oder grün. Wenn möglich, sollte ihre 'Verbindung' (z.B. zu anderen, zum Universum, zur Natur) dargestellt werden, ohne dass es sehr esoterisch wirkt.
Der Titel des Buches sollte groß genug sein, um auch als kleines Thumbnail in der Bücherfloß-Suche oder bei den Empfehlungen gelesen werden zu können. Der Name der Autorin kann klein sein. Gerne kann ein Emblem oder kleines Logo eingefügt werden, an der Stelle, an der ansonsten der Verlag steht (gerne die Sonne, die auch im Inneren des Buches als Verzierung verwendet wird – Icon hier angehängt).
Stil:
Ich lade hier eine Idee hoch, die ganz grob in die richtige Richtung geht. Die Farben (Helllila und Anthrazit) in der Kombination gefallen mir, da es weiblich, aber nicht zu süß aussieht. Die Frau sieht aber in diesem Layout nicht glücklich aus, das sollte geändert werden. Das Layout soll modern und clean, aber nicht nüchtern aussehen.

```html
<!DOCTYPE html>
<html lang="de">
<head>
<meta charset="utf-8">
<title>Allein. Getragen. Heiter. – Buchcover</title>
<link href="https://fonts.googleapis.com/css2?family=Playfair+Display:wght@600&family=Poppins:wght@600;700&family=Cormorant+Garamond:wght@600&display=swap" rel="stylesheet">
<style>
  :root {
    --page: #ffffff;
    --lilac-light: #d9b8ec;
    --lilac: #b27ccf;
    --lilac-band: #b47ecb;
    --plum: #6d4a80;
    --mauve: #9a7aa8;
    --anthracite: #1f1b22;
    --charcoal: #3a3540;
    --gold: #d7a955;
    --ink: #1e1620;
    --white: #ffffff;
  }
  html, body {
    margin: 0;
    padding: 0;
    width: 1200px;
    height: 1200px;
    overflow: hidden;
    background: var(--page);
  }
  .cover {
    position: absolute;
    left: 228px;
    top: 30px;
    width: 744px;
    height: 1140px;
    overflow: hidden;
    background: var(--lilac-band);
  }
  .cover-waves {
    position: absolute;
    left: 0;
    top: 0;
    width: 744px;
    height: 984px;
    background:
      radial-gradient(ellipse at 80% 95%, rgba(255,255,255,0.5) 0%, rgba(255,255,255,0) 45%),
      radial-gradient(ellipse at 10% 15%, var(--lilac-light) 0%, rgba(217,184,236,0) 55%),
      linear-gradient(125deg, var(--lilac) 0%, var(--plum) 40%, var(--charcoal) 62%, var(--anthracite) 78%, var(--lilac) 100%);
  }
  .cover-portrait {
    position: absolute;
    left: 42px;
    top: 468px;
    width: 460px;
    height: 516px;
    border-radius: 46% 46% 0 0;
    background:
      radial-gradient(ellipse at 45% 30%, rgba(232,214,240,0.85) 0%, rgba(190,160,205,0.7) 40%, rgba(140,110,160,0.35) 75%, rgba(140,110,160,0) 100%);
  }
  .title {
    position: absolute;
    left: 0;
    top: 0;
    width: 100%;
    height: 380px;
    margin: 0;
    text-align: center;
    font-family: "Playfair Display", serif;
    font-weight: 600;
    font-size: 98px;
    line-height: 1;
    color: var(--white);
    letter-spacing: 1px;
    text-shadow: 4px 4px 0 var(--anthracite);
  }
  .title span { position: absolute; left: 0; width: 100%; }
  .title .l1 { top: 26px; }
  .title .l2 { top: 142px; }
  .title .l3 { top: 250px; }
  .subtitle {
    position: absolute;
    left: 136px;
    top: 378px;
    display: flex;
    align-items: center;
    gap: 6px;
    color: var(--white);
    font-family: "Poppins", sans-serif;
    font-weight: 700;
    text-transform: uppercase;
  }
  .subtitle .num { font-size: 52px; line-height: 1; }
  .subtitle .text { font-size: 17px; line-height: 1.25; letter-spacing: 0.3px; }
  .badge {
    position: absolute;
    left: 476px;
    top: 528px;
    width: 212px;
    height: 212px;
    border-radius: 50%;
    background: var(--gold);
    box-shadow: 0 0 0 6px var(--white), 0 0 0 11px var(--lilac);
    display: flex;
    align-items: center;
    justify-content: center;
    text-align: center;
    font-family: "Poppins", sans-serif;
    font-weight: 600;
    font-size: 22px;
    line-height: 1.3;
    color: var(--ink);
  }
  .rule {
    position: absolute;
    left: 0;
    top: 984px;
    width: 100%;
    height: 6px;
    background: var(--gold);
    border-bottom: 3px solid var(--white);
  }
  .emblem {
    position: absolute;
    left: 354px;
    top: 1000px;
    width: 36px;
    height: 36px;
  }
  .author {
    position: absolute;
    left: 0;
    top: 1062px;
    width: 100%;
    margin: 0;
    text-align: center;
    font-family: "Cormorant Garamond", serif;
    font-weight: 600;
    font-size: 44px;
    line-height: 1;
    color: var(--ink);
  }
</style>
</head>
<body>
  <div class="cover">
    <div class="cover-waves" role="img" aria-label="Geschwungene Wellen in Helllila und Anthrazit"></div>
    <div class="cover-portrait" role="img" aria-label="Illustration: lächelnde Frau mit hellbraunem Haar, nach oben blickend"></div>

    <h1 class="title">
      <span class="l1">ALLEIN.</span>
      <span class="l2">GETRAGEN.</span>
      <span class="l3">HEITER.</span>
    </h1>

    <div class="subtitle">
      <span class="num">7</span>
      <span class="text">frische Wege zu Fülle und Nähe<br>abseits der Zweisamkeit</span>
    </div>

    <div class="badge">Mit<br>inspirierenden<br>Tipps zur<br>Umsetzung</div>

    <div class="rule"></div>

    <svg class="emblem" viewBox="0 0 36 36" aria-hidden="true">
      <circle cx="18" cy="18" r="14" fill="none" stroke="#ffffff" stroke-width="2"/>
    </svg>

    <p class="author">Jule Henrike Brandt</p>
  </div>
</body>
</html>
```